Communications Contractor Business Card Design

I would like a new business card for a new Communications company in Australia. Subcontracting and specialising in cabling, data, phone, antennas, pay tv ,modems, audio visual fibre optics etc. I am open to colour and design concepts but would like a modern clean look that stands out.

Industry/Entity Type

Tv

Contact Information for Business Card

quarzel communications pty ltd, Tomas Whitlock, PO BOX 527 Morrendale Flats QLD 4390 quarzel4me@mailbrook.net Australia. ph 0438271906. Director/Technician. services- Cabling,data,phone,antennas,audio visual,home theatre, fibre optics.

```html
<!DOCTYPE html>
<html lang="en">
<head>
<meta charset="utf-8">
<title>Quarzel Communications – Business Card</title>
<link href="https://fonts.googleapis.com/css2?family=Russo+One&family=Questrial&family=Poppins:wght@500;600;700&display=swap" rel="stylesheet">
<style>
  :root {
    --backdrop: #2b2b2d;
    --brand-red: #e0161d;
    --brand-red-dark: #c40f16;
    --teal: #2bb5b8;
    --teal-dark: #1f9ea1;
    --paper: #ffffff;
    --paper-shade: #eef0f1;
    --ink: #1c1c1c;
    --ink-soft: #3a3a3a;
  }
  * { margin: 0; padding: 0; box-sizing: border-box; }
  html, body { width: 1200px; height: 900px; overflow: hidden; }
  body {
    background: var(--backdrop);
    font-family: "Questrial", "Century Gothic", sans-serif;
    position: relative;
  }

  .card {
    position: absolute;
    width: 580px;
    height: 340px;
    overflow: hidden;
    box-shadow: 0 18px 40px rgba(0,0,0,.55);
  }

  /* Front */
  .card-front {
    left: 80px; top: 90px;
    background: linear-gradient(160deg, var(--brand-red) 0%, var(--brand-red-dark) 100%);
  }
  .card-front .brand-name {
    position: absolute;
    left: 0; right: 0; top: 95px;
    text-align: center;
    font-family: "Russo One", sans-serif;
    color: var(--paper);
    font-size: 40px;
    line-height: 1.02;
    letter-spacing: 1px;
    text-transform: uppercase;
  }
  .card-front .tagline-band {
    position: absolute;
    left: 0; right: 0; top: 262px;
    height: 42px;
    background: var(--paper-shade);
    display: flex; align-items: center; justify-content: center;
  }
  .tagline {
    font-family: "Russo One", sans-serif;
    color: var(--brand-red);
    font-size: 16px;
    letter-spacing: 2px;
    text-transform: uppercase;
  }

  /* Back */
  .card-back {
    left: 540px; top: 470px;
    background: var(--teal);
  }
  .card-back .back-shape { position: absolute; inset: 0; }
  .card-back .top-strip {
    position: absolute; left: 0; right: 0; top: 0; height: 8px;
    background: var(--teal);
  }
  .card-back .brand-name {
    position: absolute;
    left: 110px; top: 42px;
    font-family: "Russo One", sans-serif;
    color: var(--brand-red);
    font-size: 27px;
    line-height: 1.02;
    text-transform: uppercase;
  }
  .holder {
    position: absolute;
    right: 40px; top: 122px;
    text-align: right;
  }
  .holder-name {
    font-family: "Poppins", sans-serif;
    font-weight: 600;
    font-size: 20px;
    color: var(--ink);
  }
  .holder-role {
    display: inline-block;
    margin-top: 2px;
    padding: 2px 12px;
    border-radius: 10px;
    background: var(--teal);
    color: var(--paper);
    font-size: 12px;
  }
  .contact {
    position: absolute;
    left: 42px; top: 168px;
    list-style: none;
    color: var(--ink-soft);
    font-size: 16px;
    line-height: 1.3;
  }
  .contact li { display: flex; align-items: flex-start; gap: 12px; margin-bottom: 8px; }
  .contact svg { flex: none; margin-top: 2px; }
  .services-title {
    position: absolute;
    left: 290px; top: 206px;
    width: 170px;
    text-align: center;
    font-family: "Poppins", sans-serif;
    font-weight: 700;
    font-size: 16px;
    color: var(--ink);
  }
  .services-list {
    position: absolute;
    left: 0; right: 0; top: 258px;
    text-align: center;
    color: var(--paper);
    font-size: 19px;
    line-height: 1.55;
  }
</style>
</head>
<body>

<section class="card card-front" aria-label="Business card front">
  <h1 class="brand-name">Quarzel<br>Communications<br>Pty Ltd</h1>
  <div class="tagline-band">
    <p class="tagline">For all your communications requirements</p>
  </div>
</section>

<section class="card card-back" aria-label="Business card back">
  <svg class="back-shape" width="580" height="340" viewBox="0 0 580 340" aria-hidden="true">
    <path d="M0 0 H580 V198 H495 Q478 198 474 214 L470 228 Q465 242 448 242 H0 Z" fill="var(--paper)"/>
  </svg>
  <div class="top-strip"></div>

  <h2 class="brand-name">Quarzel<br>Communications Pty Ltd</h2>

  <div class="holder">
    <p class="holder-name">Tomas Whitlock</p>
    <p class="holder-role">Director/Technician</p>
  </div>

  <ul class="contact">
    <li>
      <svg width="22" height="18" viewBox="0 0 22 18" aria-label="Phone">
        <path d="M2 6 Q11 -1 20 6 L18 9 L14 7 V5 H8 V7 L4 9 Z" fill="var(--teal)"/>
        <rect x="4" y="9" width="14" height="8" rx="2" fill="var(--teal)"/>
        <circle cx="11" cy="13" r="2" fill="var(--paper)"/>
      </svg>
      <span>0438271906</span>
    </li>
    <li>
      <svg width="22" height="26" viewBox="0 0 22 26" aria-label="Location">
        <path d="M11 1 C5 1 2 5.5 2 10 C2 16 11 25 11 25 C11 25 20 16 20 10 C20 5.5 17 1 11 1 Z" fill="var(--teal)"/>
        <circle cx="11" cy="10" r="3.5" fill="var(--paper)"/>
      </svg>
      <span>PO BOX 527 Morrendale Flats,<br>QLD 4390 Australia</span>
    </li>
  </ul>

  <p class="services-title">OUR SERVICES</p>
  <p class="services-list">Data / Cabling / Phone / Antennas,<br>Audio Visual / Home Theatre / Fibre Optics.</p>
</section>

</body>
</html>
```